Data Analytics Platform Website Design

Website design for a new data analytics platform called Metrica Core. I need a design that is simple but informative, professional but still sexy and that is aimed at the business professional instead of being "technical". I have a logo (picture uploaded) and also screenshots from the platform itself and I can also provide example websites from competitors that are similar in design and layout to what I need. I also have the messaging but I need help with photos, icons, font, layout, etc. I want to utilize some of the colors in the logo, but I want the overall color scheme to utilize darker blues (more serious feeling, less playful) with one accent color for highlighting. This design cannot be "fun", "playful", or "cheerful" and should instead be "professional", "serious", but still uncluttered and clean cut. However, simple does not mean easy because I want to see transitions that are clean and high level. I want the final design to be all of that while showing the company and our product as capable, serious, and reliable.

Example websites:
1. www.valdrenix.com
2. q7.ai
3. corvelane.com
4. https://www.pym.com/en_us/software/lorsa.html
5. https://www.belvoro.com/
6. gwendel.ai

Target Market(s)

Business Professionals - Government/large companies/data analytics focused

Industry/Entity Type

Data Science

Number of Pages Required

3 page

Font styles to use
Serif
Sans Serif

Requirements
Must have
• It must be clean and professional. Cannot be cluttered or too "busy". No playful or childish looks at all.
Nice to have
• I want to see professional designs but also professional concepts incorporated.
Should not have
• Should not have Comic Sans or the like, no playful or "techy" themes

```html
<!DOCTYPE html>
<html lang="en">
<head>
<meta charset="utf-8">
<title>Metrica Core</title>
<link rel="stylesheet" href="https://fonts.googleapis.com/css2?family=Poppins:wght@300;400;500;600;700;800&family=Mulish:wght@400;600;700&display=swap">
<style>
:root{
  --navy:#0f2550;
  --navy-mid:#173a78;
  --blue:#1f4fa3;
  --blue-deep:#163f88;
  --accent:#2f6fd6;
  --ink:#1d2433;
  --text:#3a4150;
  --soft:#edf2f9;
  --blob:#d3deee;
  --white:#ffffff;
  --icon-a:#1d5fb8;
  --icon-b:#d9651c;
  --icon-c:#2f7a3a;
  --bar:#0f2550;
}
*{margin:0;padding:0;box-sizing:border-box}
html,body{width:1200px;height:3520px;overflow:hidden;background:var(--white)}
body{position:relative;font-family:"Mulish",sans-serif;color:var(--text)}
.abs{position:absolute}
.btn{position:absolute;display:flex;align-items:center;justify-content:center;border-radius:26px;font-family:"Poppins",sans-serif;font-weight:600;font-size:16px;letter-spacing:.3px;color:var(--white);background:linear-gradient(90deg,var(--blue-deep),var(--accent));box-shadow:0 6px 14px rgba(15,37,80,.22);white-space:nowrap}
.heading{font-family:"Poppins",sans-serif;font-weight:600;color:var(--ink)}

/* header */
.site-header{left:0;top:0;width:1200px;height:74px;background:var(--white)}
.brand{left:161px;top:16px;display:flex;align-items:center;gap:14px}
.brand-mark{width:36px;height:36px;background:var(--navy-mid);display:block}
.brand-name{font-family:"Poppins",sans-serif;font-weight:300;font-size:36px;letter-spacing:1.5px;color:var(--ink)}
.contact-btn{left:870px;top:19px;width:128px;height:36px;font-size:13px}
.menu{left:1014px;top:26px;width:24px}
.menu span{display:block;height:3px;background:var(--ink);margin-bottom:6px;border-radius:2px}

/* hero */
.hero{left:0;top:74px;width:1200px;height:560px}
.hero-title{left:161px;top:120px;font-family:"Poppins",sans-serif;font-weight:800;font-size:46px;line-height:54px;color:var(--white)}
.hero-sub{left:161px;top:232px;font-family:"Poppins",sans-serif;font-weight:600;font-size:32px;color:var(--white)}
.hero-btn{left:161px;top:296px;width:167px;height:44px;background:var(--white);color:var(--blue-deep);box-shadow:none}
.device{left:608px;top:109px;width:540px;height:330px}

/* sections */
.icon-badge{width:55px;height:55px;border-radius:50%;background:linear-gradient(135deg,var(--blue-deep),var(--accent));display:flex;align-items:center;justify-content:center}
.sec-title{font-size:35px;white-space:nowrap}
.sec-text{font-family:"Mulish",sans-serif;font-weight:400;font-size:21px;line-height:32px;color:var(--text)}

/* features */
.card{position:absolute;top:2091px;width:271px;height:301px;background:var(--white);border-radius:0 80px 0 80px;box-shadow:4px 6px 14px rgba(15,37,80,.07);text-align:center}
.card .ico{width:123px;height:123px;border-radius:50%;margin:30px auto 0;display:flex;align-items:center;justify-content:center}
.card h3{font-family:"Mulish",sans-serif;font-weight:700;font-size:15px;color:var(--ink);margin-top:31px}
.card p{font-size:13px;line-height:19px;color:#444;margin:8px 26px 0}

/* clients */
.client{position:absolute;top:2779px;width:141px;height:142px;background:var(--white);border-radius:71px 0 71px 71px;display:flex;align-items:center;justify-content:center;gap:7px;font-family:"Mulish",sans-serif;font-weight:700;font-size:22px;color:var(--ink);white-space:nowrap;box-shadow:2px 4px 10px rgba(15,37,80,.05)}
.client i{width:12px;height:12px;border-radius:50%;background:var(--navy-mid);display:block;flex:none}
.arrow{position:absolute;top:2852px;width:38px;height:38px;border-radius:50%;background:var(--blue-deep);display:flex;align-items:center;justify-content:center}

/* footer */
.foot-col{position:absolute;top:3195px}
.foot-col h4{font-family:"Poppins",sans-serif;font-weight:600;font-size:17px;color:var(--ink);padding-bottom:10px;border-bottom:1px solid #ddd;display:inline-block;position:relative}
.foot-col h4::after{content:"";position:absolute;left:0;bottom:-1px;width:26px;height:3px;background:var(--accent)}
.foot-col p,.foot-col li{font-size:12.5px;line-height:21px;color:#333}
.foot-col ul{list-style:none;margin-top:22px}
.foot-col ul li{margin-bottom:9px}
.foot-col ul li::before{content:"»";margin-right:10px}
.social{display:flex;align-items:center;gap:12px;margin-bottom:16px;font-size:13px}
.social i{width:28px;height:28px;border-radius:50%;background:var(--navy-mid);display:block}
.copyright{left:0;top:3476px;width:1200px;height:44px;background:var(--bar);color:var(--white);font-size:13px;display:flex;align-items:center;justify-content:center}
</style>
</head>
<body>

<header class="abs site-header">
  <div class="abs brand">
    <i class="brand-mark"></i>
    <span class="brand-name">Metrica Core</span>
  </div>
  <div class="btn contact-btn">CONTACT US</div>
  <div class="abs menu"><span></span><span></span><span></span></div>
</header>

<section class="abs hero">
  <svg class="abs" style="left:0;top:0" width="1200" height="560" viewBox="0 0 1200 560">
    <defs><linearGradient id="heroGrad" x1="0" y1="0" x2="1" y2="1"><stop offset="0" stop-color="#0f2550"/><stop offset="1" stop-color="#1f4a94"/></linearGradient></defs>
    <path d="M0 0H1200V505C1080 560 960 560 820 545C680 520 560 470 380 470C220 470 110 500 0 505Z" fill="url(#heroGrad)"/>
  </svg>
  <h1 class="abs hero-title">Speed, Capability,<br>Scale.</h1>
  <div class="abs hero-sub">No Compromising</div>
  <div class="btn hero-btn">GET STARTED</div>
  <svg class="abs device" viewBox="0 0 540 330" role="img" aria-label="Metrica Core platform dashboard on a laptop">
    <rect x="51" y="0" width="445" height="310" rx="8" fill="#f6f7fb"/>
    <rect x="70" y="18" width="86" height="272" fill="#1a2236"/>
    <rect x="166" y="36" width="310" height="200" fill="#ffffff"/>
    <rect x="178" y="95" width="58" height="10" rx="2" fill="#2f6fd6"/>
    <rect x="0" y="306" width="540" height="12" rx="6" fill="#cfd4de"/>
  </svg>
</section>

<!-- intro -->
<div class="abs" style="left:68px;top:679px;width:455px;height:408px" role="img" aria-label="Photo of two colleagues reviewing analytics charts">
  <svg width="455" height="408" viewBox="0 0 455 408">
    <ellipse cx="55" cy="48" rx="30" ry="40" fill="var(--blob)"/>
    <ellipse cx="420" cy="330" rx="34" ry="28" fill="var(--blob)"/>
    <path d="M120 10C200-10 320 0 390 60C460 130 440 260 380 330C320 400 200 420 120 380C40 340 0 260 10 170C20 80 60 25 120 10Z" fill="#8d9bb3"/>
  </svg>
</div>
<div class="abs icon-badge" style="left:581px;top:724px">
  <svg width="30" height="26" viewBox="0 0 30 26"><path d="M8 16a6 6 0 0 1 1-12 8 8 0 0 1 14 3 5 5 0 0 1-1 9Z" fill="#fff"/><g stroke="#fff" stroke-width="2"><line x1="10" y1="19" x2="10" y2="24"/><line x1="15" y1="19" x2="15" y2="24"/><line x1="20" y1="19" x2="20" y2="24"/></g></svg>
</div>
<h2 class="abs heading sec-title" style="left:581px;top:798px">What Is Metrica Core?</h2>
<p class="abs sec-text" style="left:581px;top:852px;width:480px">Metrica Core is a cloud-native data management and analysis environment where we bring all the tools to your fingertips</p>
<div class="btn" style="left:581px;top:985px;width:182px;height:44px">GET STARTED</div>

<!-- offer band -->
<svg class="abs" style="left:0;top:1195px" width="1200" height="745" viewBox="0 0 1200 745">
  <path d="M0 50C150 10 300 0 480 20C650 40 760 95 930 95C1050 95 1130 60 1200 40V640C1100 690 980 750 780 730C560 710 420 640 260 640C150 640 70 660 0 680Z" fill="var(--soft)"/>
</svg>
<div class="abs icon-badge" style="left:161px;top:1387px">
  <svg width="30" height="30" viewBox="0 0 30 30" fill="#fff"><rect x="10" y="2" width="10" height="9"/><rect x="2" y="20" width="8" height="7"/><rect x="11" y="20" width="8" height="7"/><rect x="20" y="20" width="8" height="7"/><path d="M14 11h2v4h9v5h-2v-3H7v3H5v-5h9Z"/></svg>
</div>
<h2 class="abs heading sec-title" style="left:161px;top:1462px">What Do We Offer?</h2>
<p class="abs sec-text" style="left:161px;top:1515px;width:450px;font-size:20px">We can help make it easier for you to store, query, work with, and present your data, no matter how large or small your datasets or computation needs may be.</p>
<div class="btn" style="left:161px;top:1678px;width:182px;height:44px">GET STARTED</div>
<div class="abs" style="left:677px;top:1394px;width:452px;height:407px" role="img" aria-label="Photo of team hands working over laptop with analytics charts">
  <svg width="452" height="407" viewBox="0 0 452 407">
    <ellipse cx="52" cy="60" rx="32" ry="44" fill="var(--blob)"/>
    <ellipse cx="420" cy="330" rx="32" ry="28" fill="var(--blob)"/>
    <path d="M130 10C230-8 350 0 400 60C450 130 430 240 390 310C340 390 230 410 150 380C70 350 10 300 5 200C0 110 50 25 130 10Z" fill="#7d7469"/>
  </svg>
</div>

<!-- features -->
<h2 class="abs heading sec-title" style="left:0;top:2008px;width:1200px;text-align:center">What Is Metrica Core?</h2>
<div class="card" style="left:161px">
  <div class="ico" style="background:var(--icon-a)">
    <svg width="70" height="60" viewBox="0 0 70 60" fill="none" stroke="#fff" stroke-width="3"><path d="M35 16c-8-10-24-10-24 0s16 10 24 0 24-10 24 0-16 10-24 0Z"/><circle cx="35" cy="45" r="9"/><path d="M35 45l4-4M14 36v18M10 40l4-4 4 4M56 36v18M52 40l4-4 4 4"/></svg>
  </div>
  <h3>No Limitations</h3>
  <p>An environment where there are no limitations on speed, compute, or analytics.</p>
</div>
<div class="card" style="left:466px">
  <div class="ico" style="background:var(--icon-b)">
    <svg width="64" height="60" viewBox="0 0 64 60" fill="none" stroke="#fff" stroke-width="3"><circle cx="32" cy="14" r="8"/><circle cx="16" cy="20" r="6"/><circle cx="48" cy="20" r="6"/><path d="M8 40l14-8 10 6 10-6 14 8-14 12H22Z"/></svg>
  </div>
  <h3>No Compromise</h3>
  <p>We scale with you without compromising service.</p>
</div>
<div class="card" style="left:769px">
  <div class="ico" style="background:var(--icon-c)">
    <svg width="64" height="60" viewBox="0 0 64 60" fill="none" stroke="#fff" stroke-width="3"><rect x="6" y="14" width="52" height="42"/><line x1="6" y1="22" x2="58" y2="22"/><circle cx="32" cy="8" r="5"/><circle cx="32" cy="40" r="10"/><path d="M32 40l5-5"/></svg>
  </div>
  <h3>Accelerate Your Decision</h3>
  <p>Accelerate your decision-making process seamlessly at a greater scale without having to worry about loss of speed or security.</p>
</div>
<div class="btn" style="left:508px;top:2434px;width:184px;height:44px">GET STARTED</div>

<!-- clients -->
<svg class="abs" style="left:0;top:2580px" width="1200" height="540" viewBox="0 0 1200 540">
  <path d="M0 20C200 80 420 90 640 50C860 10 1050 0 1200 20V480C1050 530 880 540 700 510C500 480 360 430 200 440C110 445 50 460 0 470Z" fill="var(--soft)"/>
</svg>
<h2 class="abs heading sec-title" style="left:0;top:2698px;width:1200px;text-align:center">Our Clients</h2>
<div class="arrow" style="left:90px"><svg width="12" height="14" viewBox="0 0 12 14"><path d="M9 1L3 7l6 6" stroke="#fff" stroke-width="2.5" fill="none"/></svg></div>
<div class="client" style="left:161px"><i></i>Tresk</div>
<div class="client" style="left:344px;font-size:15px"><i></i>Norvane Haus</div>
<div class="client" style="left:527px"><i></i>Ovira</div>
<div class="client" style="left:710px"><i></i>Idelo</div>
<div class="client" style="left:893px;font-size:18px"><i></i>Firmstead</div>
<div class="arrow" style="left:1066px"><svg width="12" height="14" viewBox="0 0 12 14"><path d="M3 1l6 6-6 6" stroke="#fff" stroke-width="2.5" fill="none"/></svg></div>

<!-- footer -->
<footer>
  <div class="foot-col" style="left:161px;width:260px">
    <h4>About Metrica Core</h4>
    <p style="margin-top:22px">Lorem Ipsum is simply dummy text of the printing and typesetting industry Ipsum has been the industry's standard dummy text ever since the 1500s, when an unknown printer took a galley of type</p>
  </div>
  <div class="foot-col" style="left:481px">
    <h4>Quick Links</h4>
    <ul>
      <li>What Is Metrica Core?</li>
      <li>What Do We Offer?</li>
      <li>How Are We Different?</li>
      <li>Contact Us</li>
    </ul>
  </div>
  <div class="foot-col" style="left:702px;width:200px">
    <h4>Contact Details</h4>
    <div style="display:flex;gap:8px;margin-top:22px">
      <svg width="12" height="16" viewBox="0 0 12 16"><path d="M6 0a6 6 0 0 1 6 6c0 4-6 10-6 10S0 10 0 6a6 6 0 0 1 6-6Z" fill="var(--navy-mid)"/><circle cx="6" cy="6" r="2" fill="#fff"/></svg>
      <p>482 Harlow Station Rd.<br>Building, AR 723194</p>
    </div>
    <div style="display:flex;gap:8px;margin-top:10px">
      <svg width="14" height="14" viewBox="0 0 14 14"><path d="M3 0l3 3-2 2a9 9 0 0 0 5 5l2-2 3 3-2 3C6 14 0 8 0 2Z" fill="var(--navy-mid)"/></svg>
      <p><b style="font-weight:700">PHONE</b><br>+01 555 204 7781</p>
    </div>
    <div style="display:flex;gap:8px;margin-top:10px">
      <svg width="14" height="11" viewBox="0 0 14 11"><rect width="14" height="11" fill="var(--navy-mid)"/><path d="M0 0l7 6 7-6" stroke="#fff" fill="none"/></svg>
      <p><b style="font-weight:700">EMAIL</b><br>info@metricacore.com</p>
    </div>
  </div>
  <div class="foot-col" style="left:932px">
    <h4>Follow Us</h4>
    <div style="margin-top:22px">
      <div class="social"><i></i>Linkfold</div>
      <div class="social"><i></i>Chirpwell</div>
      <div class="social"><i></i>Viewcast</div>
      <div class="social"><i></i>Snapframe</div>
    </div>
  </div>
</footer>
<div class="abs copyright">Copyright © 2021 Metrica Core. All Rights Reserved.</div>

</body>
</html>
```